Bright Reach Hoists

im looking for someone to help me with my letterhead design. i have already got my logo design just need help with this part

Industry/Entity Type

Construction

Colors
0255a3

Requirements
Must have
• must have all my details eg. bank details, abn and acn

```html
<!DOCTYPE html>
<html lang="en">
<head>
<meta charset="utf-8">
<title>Bright Reach Hoists — Letterhead</title>
<link href="https://fonts.googleapis.com/css2?family=Roboto+Slab:wght@400;600&display=swap" rel="stylesheet">
<style>
  :root {
    --brand-blue: #1a75bc;
    --ink: #1b1b1b;
    --text-grey: #3a3a3a;
    --rule-grey: #555555;
    --paper: #ffffff;
    --watermark: #eef1f4;
  }
  * { box-sizing: border-box; margin: 0; padding: 0; }
  html, body { width: 950px; height: 1200px; overflow: hidden; background: var(--paper); }
  .letterhead {
    position: relative;
    width: 950px;
    height: 1200px;
    background: var(--paper);
    font-family: "Roboto Slab", serif;
    overflow: hidden;
  }
  .brand {
    position: absolute;
    left: 24px;
    top: 36px;
    display: flex;
    align-items: center;
    gap: 12px;
  }
  .brand-square {
    width: 26px;
    height: 26px;
    background: var(--brand-blue);
  }
  .brand-name {
    font-size: 27px;
    font-weight: 600;
    color: var(--ink);
    letter-spacing: 0.3px;
  }
  .address {
    position: absolute;
    left: 668px;
    top: 28px;
    height: 58px;
    border-left: 1.5px solid var(--rule-grey);
    padding-left: 22px;
    display: flex;
    gap: 8px;
  }
  .address-icon { width: 20px; height: 20px; margin-top: 4px; flex: none; }
  .address-text {
    font-size: 18px;
    line-height: 26px;
    color: var(--text-grey);
  }
  .watermark {
    position: absolute;
    left: 0;
    right: 0;
    top: 490px;
    text-align: center;
    font-size: 74px;
    font-weight: 600;
    color: var(--watermark);
    letter-spacing: 1px;
  }
  .footer {
    position: absolute;
    left: 0;
    bottom: 0;
    width: 950px;
    height: 100px;
  }
  .footer-shape { position: absolute; inset: 0; width: 950px; height: 100px; }
  .footer-row {
    position: absolute;
    left: 0;
    right: 0;
    display: flex;
    justify-content: center;
    align-items: center;
    color: var(--paper);
    font-size: 15px;
  }
  .registration { top: 31px; }
  .contacts { top: 64px; }
  .footer-item { display: flex; align-items: center; gap: 7px; padding: 0 24px; }
  .footer-item + .footer-item { border-left: 1px solid rgba(255,255,255,0.55); }
  .footer-icon { width: 18px; height: 18px; flex: none; }
</style>
</head>
<body>
<main class="letterhead">
  <header>
    <div class="brand">
      <span class="brand-square"></span>
      <span class="brand-name">Bright Reach Hoists</span>
    </div>
    <div class="address">
      <svg class="address-icon" viewBox="0 0 20 20" aria-hidden="true">
        <path d="M10 2 L1 10 H4 V18 H8.5 V13 H11.5 V18 H16 V10 H19 Z" fill="var(--brand-blue)"/>
      </svg>
      <p class="address-text">Street Name, City Name<br>State Zipcode</p>
    </div>
  </header>

  <div class="watermark" aria-hidden="true">Bright Reach Hoists</div>

  <footer class="footer">
    <svg class="footer-shape" viewBox="0 0 950 100" preserveAspectRatio="none" aria-hidden="true">
      <path d="M0 62 Q475 -56 950 62" fill="none" stroke="#111" stroke-width="3"/>
      <path d="M0 68 Q475 -37 950 68 L950 100 L0 100 Z" fill="var(--brand-blue)"/>
    </svg>
    <div class="footer-row registration">
      <span class="footer-item">ABN 12 456 578 655</span>
      <span class="footer-item">ACN 12 456 578 655</span>
    </div>
    <div class="footer-row contacts">
      <span class="footer-item">
        <svg class="footer-icon" viewBox="0 0 18 18" aria-hidden="true">
          <circle cx="9" cy="9" r="8" fill="none" stroke="#fff" stroke-width="1.2"/>
          <path d="M7 4.5 L5.5 6 C5.5 9.5 8.5 12.5 12 12.5 L13.5 11 L11.5 9.5 L10.3 10.5 C9 10 8 9 7.5 7.7 L8.5 6.5 Z" fill="#fff"/>
        </svg>
        123-456-7890
      </span>
      <span class="footer-item">
        <svg class="footer-icon" viewBox="0 0 18 18" aria-hidden="true">
          <rect x="1" y="4" width="16" height="11" fill="#fff"/>
          <path d="M1 4 L9 10.5 L17 4" fill="none" stroke="var(--brand-blue)" stroke-width="1.3"/>
        </svg>
        hello@brightreachhoists.com
      </span>
      <span class="footer-item">
        <svg class="footer-icon" viewBox="0 0 18 18" aria-hidden="true">
          <g fill="none" stroke="#fff" stroke-width="1.1">
            <circle cx="9" cy="9" r="7.5"/>
            <ellipse cx="9" cy="9" rx="3.3" ry="7.5"/>
            <path d="M1.5 9 H16.5 M2.8 5 H15.2 M2.8 13 H15.2"/>
          </g>
        </svg>
        www.brightreachhoists.com
      </span>
    </div>
  </footer>
</main>
</body>
</html>
```